Design NEW business card

We would like a business card using the colour deep red wine or dark navy blue textured background (patterned or not, open to suggestions) with a high gloss debossed rose gold/copper TM Thomas Marlow Jewellery business name (Provided). I have included images for your review we would like to keep our currently logo and business name on the front but you can change the layout and positioning. For the back of the card we are open to all suggestions/variations.
Use our current TM Thomas Marlow Jewellery logo (Provided image)

```html
<!DOCTYPE html>
<html lang="en">
<head>
<meta charset="utf-8">
<title>Thomas Marlow Jewellery – Business Card</title>
<link rel="stylesheet" href="https://fonts.googleapis.com/css2?family=Montserrat:wght@300;400&display=swap">
<style>
  :root {
    --page-bg: #e4e2df;
    --wine: #521f27;
    --wine-deep: #3a151b;
    --card-white: #f7f6f4;
    --rose-gold: #c8977a;
    --rose-gold-soft: #d3a88d;
  }
  * { box-sizing: border-box; margin: 0; padding: 0; }
  html, body {
    width: 1200px;
    height: 900px;
    overflow: hidden;
    background: var(--page-bg);
    font-family: "Montserrat", sans-serif;
  }
  .sheet {
    width: 1200px;
    height: 900px;
    display: flex;
    flex-direction: column;
    align-items: center;
    justify-content: center;
    gap: 30px;
  }
  .card {
    width: 700px;
    height: 400px;
    position: relative;
    box-shadow: 0 6px 18px rgba(0, 0, 0, 0.18);
  }
  .card--front {
    background: linear-gradient(120deg, var(--wine) 0%, var(--wine) 45%, var(--wine-deep) 100%);
    display: flex;
    align-items: center;
    justify-content: center;
  }
  .brand {
    display: flex;
    align-items: center;
    gap: 26px;
    color: var(--rose-gold);
    font-weight: 300;
  }
  .brand__dot {
    width: 74px;
    height: 74px;
    border-radius: 50%;
    border: 2px solid var(--rose-gold);
  }
  .brand__name {
    display: flex;
    flex-direction: column;
    gap: 10px;
  }
  .brand__line {
    font-size: 34px;
    letter-spacing: 0.2em;
    text-transform: uppercase;
  }
  .brand__sub {
    font-size: 15px;
    letter-spacing: 1.05em;
    text-transform: uppercase;
  }
  .card--back {
    background: var(--card-white);
    display: flex;
    flex-direction: column;
    align-items: center;
    justify-content: center;
    color: var(--rose-gold);
    text-align: center;
  }
  .contact__name {
    font-size: 24px;
    font-weight: 400;
    letter-spacing: 0.06em;
    text-transform: uppercase;
  }
  .contact__role {
    font-size: 12px;
    letter-spacing: 0.08em;
    text-transform: uppercase;
    margin-top: 4px;
  }
  .contact__rule {
    width: 26px;
    height: 1px;
    background: var(--rose-gold-soft);
    margin: 16px 0;
  }
  .contact__details {
    list-style: none;
    font-size: 14px;
    line-height: 1.5;
    letter-spacing: 0.04em;
  }
</style>
</head>
<body>
  <main class="sheet">
    <section class="card card--front" aria-label="Card front">
      <div class="brand">
        <span class="brand__dot" aria-hidden="true"></span>
        <div class="brand__name">
          <span class="brand__line">Thomas Marlow</span>
          <span class="brand__sub">Jewellery</span>
        </div>
      </div>
    </section>
    <section class="card card--back" aria-label="Card back">
      <h1 class="contact__name">Daniel Reed</h1>
      <p class="contact__role">CEO/Founder</p>
      <span class="contact__rule" aria-hidden="true"></span>
      <ul class="contact__details">
        <li>555 218 4097</li>
        <li>hello@marlowjewels.com</li>
        <li>www.marlowjewels.com</li>
      </ul>
    </section>
  </main>
</body>
</html>
```